Package design for supplement

We are looking to design a product packaing in Paperboard Jar. Our company sells varity of supplements. we had previously design in Stand up pouches but we needs new design in Jars. See attached all product information and logos

```html
<!DOCTYPE html>
<html lang="en">
<head>
<meta charset="utf-8">
<title>Verdalo Naturals – Organic Psyllium Whole Husk Jar Label</title>
<link rel="stylesheet" href="https://fonts.googleapis.com/css2?family=Cinzel:wght@500;600&family=Lato:wght@400;700&display=swap">
<style>
  :root {
    --backdrop: #737373;
    --paper: #f3f6ee;
    --wash: #d9ecc8;
    --wash-deep: #c8e2b2;
    --title-green: #1c8a3c;
    --brand-slate: #3c5360;
    --gold: #c99a2e;
    --gold-light: #f2d98a;
    --green-1: #4aa64a;
    --green-2: #1f9440;
    --green-3: #0f7a2e;
    --green-4: #06591f;
    --green-5: #033f15;
    --sprig: #a9d68f;
    --white: #ffffff;
  }
  * { box-sizing: border-box; margin: 0; padding: 0; }
  html, body { width: 1200px; height: 1081px; overflow: hidden; }
  body { background: var(--backdrop); position: relative; font-family: "Lato", sans-serif; }

  .jar-label {
    position: absolute; left: 423px; top: 247px;
    width: 354px; height: 587px;
    background: var(--paper);
    overflow: hidden;
  }
  .label-art { position: absolute; inset: 0; }

  .lid-title, .product-title, .brand-name {
    position: absolute; left: 0; width: 100%;
    text-align: center; font-family: "Cinzel", serif; font-weight: 600;
  }
  .lid-title { top: 66px; font-size: 16px; line-height: 18px; color: var(--title-green); }
  .product-title { top: 312px; left: 70px; width: 204px; font-size: 25px; line-height: 27px; color: var(--title-green); }
  .brand-name { top: 178px; color: var(--brand-slate); }
  .brand-name .brand-word { display: block; font-size: 40px; line-height: 44px; letter-spacing: 2px; }
  .brand-name .brand-sub { display: block; font-size: 11px; letter-spacing: 9px; padding-left: 60px; }

  .net-weight {
    position: absolute; top: 538px; left: 0; width: 100%;
    text-align: center; color: var(--white); font-size: 12px; line-height: 14px;
  }
  .net-weight strong { display: block; font-weight: 700; font-size: 12px; }

  .plant-sprig {
    position: absolute; left: 212px; top: 332px; width: 126px; height: 172px;
    background: radial-gradient(ellipse at 45% 45%, rgba(169,214,143,0.55), rgba(169,214,143,0) 70%);
  }
</style>
</head>
<body>
  <div class="jar-label">
    <svg class="label-art" width="354" height="587" viewBox="0 0 354 587" aria-hidden="true">
      <defs>
        <linearGradient id="goldBand" x1="0" y1="0" x2="0" y2="1">
          <stop offset="0" stop-color="#a87a1c"/>
          <stop offset="0.5" stop-color="#f2d98a"/>
          <stop offset="1" stop-color="#a87a1c"/>
        </linearGradient>
        <linearGradient id="goldRing" x1="0" y1="0" x2="1" y2="1">
          <stop offset="0" stop-color="#c99a2e"/>
          <stop offset="0.5" stop-color="#f2d98a"/>
          <stop offset="1" stop-color="#c99a2e"/>
        </linearGradient>
      </defs>
      <!-- lid section wash -->
      <rect x="0" y="0" width="354" height="147" fill="var(--paper)"/>
      <path d="M40 0 H354 V40 C320 55 300 45 280 70 C300 100 330 110 354 120 V147 H0 V110 C30 100 60 112 90 95 C70 70 50 40 40 0 Z" fill="var(--wash)"/>
      <!-- body wash -->
      <rect x="0" y="157" width="354" height="430" fill="var(--wash)"/>
      <path d="M0 170 C25 200 20 240 35 280 C20 330 10 360 0 380 Z" fill="var(--paper)"/>
      <path d="M354 157 V300 C330 280 320 240 300 215 C320 190 340 175 354 157 Z" fill="var(--paper)" opacity="0.7"/>
      <!-- gold bands -->
      <rect x="0" y="147" width="354" height="10" fill="url(#goldBand)"/>
      <!-- emblem ring -->
      <circle cx="172" cy="363" r="96" fill="none" stroke="url(#goldRing)" stroke-width="2"/>
      <circle cx="172" cy="363" r="90" fill="none" stroke="url(#goldRing)" stroke-width="0.8" opacity="0.7"/>
      <!-- green waves -->
      <path d="M0 412 C110 385 240 420 354 475 V587 H0 Z" fill="var(--green-1)"/>
      <path d="M0 428 C120 405 250 440 354 490 V587 H0 Z" fill="var(--green-2)"/>
      <path d="M0 470 C130 460 260 480 354 510 V587 H0 Z" fill="var(--green-3)"/>
      <path d="M0 510 C130 505 260 515 354 530 V587 H0 Z" fill="var(--green-4)"/>
      <path d="M0 535 C130 532 260 538 354 545 V587 H0 Z" fill="var(--green-5)"/>
      <rect x="0" y="568" width="354" height="9" fill="url(#goldBand)"/>
      <rect x="0" y="577" width="354" height="10" fill="#d9dcdc"/>
      <!-- certification badges (plain) -->
      <circle cx="68" cy="488" r="16" fill="var(--white)" stroke="var(--green-3)" stroke-width="3"/>
      <circle cx="68" cy="531" r="16" fill="var(--white)" stroke="var(--green-3)" stroke-width="3"/>
    </svg>

    <p class="lid-title">Organic Psyllium<br>Whole Husk</p>

    <h2 class="brand-name">
      <span class="brand-word">VERDALO</span>
      <span class="brand-sub">NATURALS</span>
    </h2>

    <div class="plant-sprig" role="img" aria-label="Line illustration of a flowering psyllium plant sprig"></div>

    <h1 class="product-title">Organic Psyllium Whole Husk</h1>

    <p class="net-weight">Net Weight <strong>16oz (453.6g)</strong></p>
  </div>
</body>
</html>
```